Kestriva Business Card Design - double sided -plumbing local plumbing company

We have a Plumbing company where the design was create through Makerhive. We would now like a business card designed as well. We want it to be in the colour version of the logo.

Details below for the card.

Phone Number: 0468 215 374
Email: info@kestrivapipeworks.com.au
Website: https://kestrivapipeworks.com.au
We really want a sophisticated design that stand out from the other- informative and timeless.

Target Market(s)

local Canberra market

Industry/Entity Type

Plumbing, gas fitting, hot water

Contact Information for Business Card

Phone number, email, logo and "Supplying all your heating, cooling and hot water needs"

Requirements
Must have
• bust be colourful, must also be though about it being printed on a magnet. must Flo with the logo - I dont want the logo and information chucked onto a white canvas I would prefer it to be smooth and look purposeful

```html
<!DOCTYPE html>
<html lang="en">
<head>
<meta charset="utf-8">
<title>Kestriva Plumbing – Business Card</title>
<link href="https://fonts.googleapis.com/css2?family=Montserrat:wght@400;500;700;800&display=swap" rel="stylesheet">
<style>
  :root {
    --brand-blue: #3179bf;
    --brand-blue-soft: #e8f1fa;
    --ink: #1c1c1c;
    --paper: #ffffff;
    --backdrop: #3b3b3d;
    --rule: #2a2a2a;
  }
  * { box-sizing: border-box; margin: 0; padding: 0; }
  html, body {
    width: 1200px; height: 998px; overflow: hidden;
    background: var(--backdrop);
    font-family: "Montserrat", Arial, sans-serif;
  }
  .sheet {
    width: 1200px; height: 998px;
    display: flex; flex-direction: column; align-items: center; justify-content: center;
    gap: 40px;
  }
  .card {
    position: relative;
    width: 760px; height: 434px;
    overflow: hidden;
    box-shadow: 0 14px 30px rgba(0,0,0,.45);
  }

  .wordmark {
    display: flex; align-items: center; gap: 18px;
    font-weight: 800; text-transform: uppercase; letter-spacing: 2px; line-height: 1;
  }
  .wordmark__dot { border-radius: 50%; flex: none; }
  .wordmark__sub { display: block; font-size: .42em; letter-spacing: .55em; margin-top: 10px; }

  /* Front */
  .card--front {
    background: var(--brand-blue);
    display: flex; flex-direction: column; align-items: center; justify-content: center;
    gap: 34px;
  }
  .card--front .wordmark { color: var(--paper); font-size: 64px; }
  .card--front .wordmark__dot { width: 54px; height: 54px; background: var(--paper); }
  .tagline {
    color: var(--paper); font-size: 15px; font-weight: 500; letter-spacing: .5px;
  }

  /* Back */
  .card--back {
    background: linear-gradient(160deg, var(--paper) 55%, var(--brand-blue-soft) 100%);
    color: var(--ink);
  }
  .card--back::after {
    content: ""; position: absolute; left: 0; right: 0; bottom: 0; height: 14px;
    background: var(--brand-blue);
  }
  .card--back .wordmark {
    position: absolute; left: 56px; top: 78px;
    color: var(--brand-blue); font-size: 40px; gap: 12px;
  }
  .card--back .wordmark__dot { width: 34px; height: 34px; background: var(--brand-blue); }
  .person {
    position: absolute; right: 40px; top: 170px; text-align: right;
  }
  .person__name {
    color: var(--brand-blue); font-weight: 800; font-size: 30px; text-transform: uppercase; letter-spacing: .5px;
  }
  .person__role { font-size: 15px; font-weight: 500; text-transform: uppercase; margin-top: 4px; }
  .divider {
    position: absolute; left: 150px; right: 30px; top: 262px;
    border-top: 1.5px solid var(--rule);
  }
  .address {
    position: absolute; right: 40px; top: 280px; text-align: right;
    font-size: 16px; line-height: 1.5;
  }
  .contacts {
    position: absolute; left: 150px; top: 278px;
    list-style: none; font-size: 17px; line-height: 1.55;
  }
  .contacts li { display: flex; align-items: center; gap: 12px; }
  .contacts svg { width: 17px; height: 17px; flex: none; }
  .card--back .tagline {
    position: absolute; left: 150px; bottom: 34px;
    color: var(--brand-blue); font-size: 14px; font-weight: 700;
  }
</style>
</head>
<body>
<main class="sheet">
  <section class="card card--front" aria-label="Card front">
    <div class="wordmark">
      <span class="wordmark__dot"></span>
      <span>Kestriva<span class="wordmark__sub">Plumbing</span></span>
    </div>
    <p class="tagline">Supplying all your heating, cooling and hot water needs</p>
  </section>

  <section class="card card--back" aria-label="Card back">
    <div class="wordmark">
      <span class="wordmark__dot"></span>
      <span>Kestriva<span class="wordmark__sub">Plumbing</span></span>
    </div>

    <div class="person">
      <p class="person__name">Marcus Ellery</p>
      <p class="person__role">Managing Director</p>
    </div>

    <div class="divider"></div>

    <ul class="contacts">
      <li>
        <svg viewBox="0 0 24 24" aria-hidden="true"><path fill="var(--brand-blue)" d="M6.6 10.8a15.1 15.1 0 0 0 6.6 6.6l2.2-2.2c.3-.3.7-.4 1-.2 1.1.4 2.3.6 3.6.6.6 0 1 .4 1 1V20c0 .6-.4 1-1 1A17 17 0 0 1 3 4c0-.6.4-1 1-1h3.5c.6 0 1 .4 1 1 0 1.3.2 2.5.6 3.6.1.3 0 .7-.2 1z"/></svg>
        <span>0468 215 374</span>
      </li>
      <li>
        <svg viewBox="0 0 24 24" aria-hidden="true"><rect x="2" y="5" width="20" height="14" fill="var(--brand-blue)"/><path d="M2 5l10 8 10-8" fill="none" stroke="#fff" stroke-width="1.6"/></svg>
        <span>info@kestrivapipeworks.com.au</span>
      </li>
      <li>
        <svg viewBox="0 0 24 24" aria-hidden="true"><g fill="none" stroke="var(--brand-blue)" stroke-width="2"><circle cx="12" cy="12" r="9"/><path d="M3 12h18M12 3c3 3 3 15 0 18M12 3c-3 3-3 15 0 18"/></g></svg>
        <span>kestrivapipeworks.com.au</span>
      </li>
    </ul>

    <p class="address">421, Address line goes here<br>45452, Country name</p>

    <p class="tagline">Supplying all your heating, cooling and hot water needs</p>
  </section>
</main>
</body>
</html>
```